Landing page in the senior sector

We need a landing page for families looking for retirement homes for their parent. The target is rather old (50-60 years old). The mandatory fields are Name, Email, Phone. The optional fields are budget, research zipcode, Emergency (,,). It is important to note that this is a free service that we offer to families in research. It should be noted that they are often in distress and repulsive. Need a mobile landing We need a landing page to recruit families looking for retirement homes for their parent. The target is rather old (50-60 years old). Required fields are Name, Email, Phone. The optional fields (they may not appear at all) are Budget, Search CP, Emergency (,,). It is important to mention that this is a free service that we offer to families in search. It should be noted that they are often in distress and that asking them for input may let tel may seem repulsive. Also need a mobile version

Target Market(s)

rather old (50-60 years old) / rather old (50-60 years old)

Coding

Coded - Design and coding required

Number of Pages Required

2 page

Font styles to use
Sans Serif

Colors

Designer to choose colors to be used in the design.

Requirements
Must have
• - A form with the 3 mandatory fields / A form with the 3 mandatory fields - Optimized for conversion / Optimized for conversion

```html
<!DOCTYPE html>
<html lang="en">
<head>
<meta charset="utf-8">
<title>Golden Grove Living – Certified Care for your Family</title>
<link rel="stylesheet" href="https://fonts.googleapis.com/css2?family=Roboto:wght@300;400;500;700&family=Playfair+Display:wght@700&display=swap">
<style>
  :root {
    --navy: #0d2c54;
    --blue: #0a6fc0;
    --blue-dark: #084f92;
    --green: #a3c72a;
    --lime: #c9dc3a;
    --white: #ffffff;
    --field-border: #d4d4d4;
    --placeholder: #666666;
    --note: #888888;
    --required: #e0262d;
  }
  * { box-sizing: border-box; margin: 0; padding: 0; }
  html, body { width: 1200px; height: 596px; overflow: hidden; }
  body { font-family: "Roboto", Arial, sans-serif; background: var(--white); }

  .hero { position: relative; width: 1200px; height: 596px; overflow: hidden; }
  .hero-photo {
    position: absolute; inset: 0;
    background:
      linear-gradient(90deg, rgba(0,0,0,0) 55%, rgba(190,215,40,.55) 80%, rgba(210,225,50,.75) 100%),
      radial-gradient(ellipse at 30% 20%, #e8efd8 0%, rgba(200,215,180,0) 45%),
      linear-gradient(180deg, #b9c9a4 0%, #7f9a68 40%, #4f6b52 70%, #2d3f36 100%);
  }
  .hero-photo::after {
    content: ""; position: absolute; inset: 0;
    background: linear-gradient(90deg, rgba(0,0,0,0) 70%, rgba(20,60,90,.35) 82%, rgba(0,0,0,.15) 100%);
  }

  .brand {
    position: absolute; left: 52px; top: 66px;
    display: flex; align-items: center; gap: 6px;
    font-weight: 700; font-size: 13px; color: var(--navy);
  }
  .brand-mark { width: 10px; height: 10px; background: var(--navy); }

  .call {
    position: absolute; left: 916px; top: 20px;
    display: flex; align-items: center; gap: 12px;
    font-size: 23px; font-weight: 500; color: var(--navy); letter-spacing: .5px;
  }
  .call-icon {
    width: 27px; height: 27px; border-radius: 50%; background: var(--navy);
    display: flex; align-items: center; justify-content: center;
  }

  .pitch { position: absolute; left: 152px; top: 272px; color: var(--white); }
  .pitch-kicker { font-weight: 700; font-size: 15.5px; margin-left: 5px; text-shadow: 0 1px 3px rgba(0,0,0,.4); }
  .pitch-title {
    font-family: "Playfair Display", Georgia, serif; font-weight: 700;
    font-size: 51px; line-height: 60px; margin-top: 6px;
    text-shadow: 0 2px 6px rgba(0,0,0,.35);
  }

  .reserve-card {
    position: absolute; left: 735px; top: 132px; width: 313px; height: 375px;
    background: var(--white); box-shadow: 0 4px 14px rgba(0,0,0,.25);
  }
  .reserve-head {
    height: 82px; padding: 17px 0 0 25px; color: var(--white);
    background: linear-gradient(180deg, var(--blue) 0%, var(--blue-dark) 100%);
  }
  .reserve-head p { font-size: 15.5px; font-weight: 300; }
  .reserve-head h2 { font-size: 23px; font-weight: 700; letter-spacing: 1.6px; margin-top: 2px; }

  .reserve-form { padding: 26px 17px 0 17px; position: relative; }
  .field { position: relative; margin-bottom: 13px; }
  .field:nth-child(2) { margin-bottom: 16px; }
  .field input {
    width: 279px; height: 41px; border: 1px solid var(--field-border);
    box-shadow: inset 0 1px 3px rgba(0,0,0,.12);
    padding-left: 14px; font-family: inherit; font-size: 11px; color: #333;
  }
  .field input::placeholder { color: var(--placeholder); }
  .field::after {
    content: "*"; position: absolute; right: -9px; top: -6px;
    color: var(--required); font-size: 11px;
  }
  .form-note { font-size: 9.5px; color: var(--note); margin: 3px 0 0 3px; }
  .form-note span { color: var(--required); }
  .reserve-btn {
    display: block; width: 279px; height: 40px; margin-top: 19px;
    border: 0; background: var(--green); color: var(--white);
    font-family: inherit; font-weight: 700; font-size: 13px; letter-spacing: .6px;
  }
</style>
</head>
<body>
<main class="hero">
  <div class="hero-photo" role="img" aria-label="Photo of an elderly couple walking hand in hand along a sunny country path by a wooden fence"></div>

  <div class="brand"><span class="brand-mark"></span>GOLDEN GROVE LIVING</div>

  <div class="call">
    <span class="call-icon">
      <svg width="10" height="15" viewBox="0 0 10 15" aria-hidden="true">
        <rect x="1" y="1" width="8" height="13" rx="1.5" fill="none" stroke="#fff" stroke-width="1.2"/>
        <line x1="1" y1="11" x2="9" y2="11" stroke="#fff" stroke-width="1"/>
        <circle cx="5" cy="12.5" r=".7" fill="#fff"/>
      </svg>
    </span>
    555-014-2200
  </div>

  <section class="pitch">
    <p class="pitch-kicker">WE CAN HELP YOU TODAY</p>
    <h1 class="pitch-title">Certified Care<br>for your Family</h1>
  </section>

  <section class="reserve-card">
    <header class="reserve-head">
      <p>Looking for assisted Living Home?</p>
      <h2>Reserve yours Today!</h2>
    </header>
    <form class="reserve-form">
      <div class="field"><input type="text" placeholder="Enter your name"></div>
      <div class="field"><input type="email" placeholder="Enter your email"></div>
      <div class="field"><input type="tel" placeholder="Enter your phone"></div>
      <p class="form-note"><span>*</span> marks are mandatory fields</p>
      <button type="button" class="reserve-btn">RESERVE TODAY!</button>
    </form>
  </section>
</main>
</body>
</html>
```